White Paper and One-Page Advertisement for TELVAMORE-QX

I need both documents to be better formatted and designed so they look professional, not something someone with mediocre word skills put together. They will go out to 1000s of industry professionals, and they need to look sharp. I need them to have my company's color palate logo, and branding on it similar to how it is now, but better. Please do not change any of the written content, but it can be arranged in any other format you think is better. Smart art and things i've already used can be omitted in favor of better designs. The developer is free to use their creativity. White paper should not be longer than the three pages unless necessary.

Target Market(s)

Life Sciences supply chain professionals

Colors
33b8a4
0592cd
9bcb3c
fbee3e
3277b5

Requirements
Must have
• Must be professional looking and not look like something done in word. Please use the color palate as seen on the documents.
Should not have
• Any changes to the written content.

```html
<!DOCTYPE html>
<html lang="en">
<head>
<meta charset="utf-8">
<title>TELVAMORE-QX — One-Page Advertisement</title>
<link href="https://fonts.googleapis.com/css2?family=Montserrat:wght@700;800&family=Mulish:wght@400;600;700&display=swap" rel="stylesheet">
<style>
  :root{
    --teal:#147a68;
    --green:#8cc63f;
    --green-light:#9bcb3c;
    --text:#333a3a;
    --white:#ffffff;
  }
  *{margin:0;padding:0;box-sizing:border-box}
  html,body{width:878px;height:1200px;overflow:hidden;background:var(--white)}
  .flyer{position:relative;width:878px;height:1200px;overflow:hidden;background:var(--white);
    font-family:"Mulish",sans-serif;color:var(--text)}
  .art{position:absolute;inset:0}
  .brand{position:absolute;left:584px;top:106px;font-family:"Montserrat",sans-serif;font-weight:800;
    font-size:29px;line-height:36px;color:var(--teal);letter-spacing:.5px}
  .tab{position:absolute;left:0;height:27px;padding:0 18px 0 22px;border-radius:0 14px 14px 0;
    background:linear-gradient(90deg,var(--teal) 0%,var(--teal) 55%,var(--green) 100%);
    color:var(--white);font-family:"Montserrat",sans-serif;font-weight:800;font-size:22px;line-height:27px}
  .tab--platform{top:510px;width:242px}
  .tab--promise{top:926px;width:222px}
  .tab--benefits{left:484px;top:742px;width:148px;border-radius:3px 14px 14px 3px;padding-left:8px}
  .list{position:absolute;list-style:none;font-size:12.6px;line-height:17.4px}
  .list li{position:relative;padding-left:12px;text-align:justify}
  .list li::before{content:"";position:absolute;left:1px;top:7px;width:4px;height:4px;border-radius:50%;background:var(--teal)}
  .platform{left:24px;top:553px;width:380px}
  .platform li.spaced{margin-top:17px}
  .features{left:24px;top:786px;width:380px}
  .features li{margin-bottom:16px}
  .promise{left:24px;top:968px;width:380px}
  .benefits{left:489px;top:784px;width:370px}
  .benefits li{margin-bottom:5px;text-align:left}
  .step{position:absolute;width:120px;text-align:center;font-size:12.6px;line-height:15.5px}
  .step__num{display:block;margin:0 auto 8px;width:34px;height:34px;border-radius:50%;
    background:var(--green);border:3px solid var(--teal);color:var(--white);
    font-family:"Montserrat",sans-serif;font-weight:700;font-size:19px;line-height:28px}
  .mission{position:absolute;left:25px;font-size:12.6px;line-height:16px}
  .mission strong{color:var(--teal);font-weight:700}
  .mission--aim{top:1036px;width:620px}
  .mission--steward{top:1064px;width:525px}
  .contact{position:absolute;left:663px;top:1078px;color:var(--white)}
  .contact h2{font-family:"Montserrat",sans-serif;font-weight:700;font-size:20px;
    border-bottom:2px solid var(--white);display:inline-block;line-height:24px;margin-bottom:11px}
  .contact ul{list-style:none}
  .contact li{font-size:14px;line-height:23px;display:flex;align-items:center;gap:6px}
  .contact svg{width:12px;height:12px}
</style>
</head>
<body>
<main class="flyer">
  <svg class="art" width="878" height="1200" viewBox="0 0 878 1200">
    <defs>
      <linearGradient id="ceremonyTones" x1="0" y1="0" x2="1" y2="1">
        <stop offset="0" stop-color="#6b3f2a"/><stop offset=".5" stop-color="#c59a72"/><stop offset="1" stop-color="#2f5e5a"/>
      </linearGradient>
      <linearGradient id="suitTones" x1="0" y1="0" x2="1" y2="1">
        <stop offset="0" stop-color="#3a4f70"/><stop offset=".5" stop-color="#c9a48a"/><stop offset="1" stop-color="#2a3550"/>
      </linearGradient>
      <linearGradient id="waveGreen" x1="0" y1="0" x2="1" y2="0">
        <stop offset="0" stop-color="#9bcb3c"/><stop offset="1" stop-color="#7fbf3a"/>
      </linearGradient>
    </defs>
    <!-- band and ring framing the secondary photo -->
    <circle cx="691" cy="490" r="228" fill="none" stroke="var(--teal)" stroke-width="10"/>
    <rect x="590" y="240" width="110" height="50" fill="var(--white)"/>
    <path d="M878 177 H640 C612 177 600 200 598 240 L596 283" fill="none" stroke="var(--teal)" stroke-width="10"/>
    <circle cx="691" cy="490" r="172" fill="url(#suitTones)" role="img"
      aria-label="Photo: businessman in a suit and striped tie giving a thumbs up"/>
    <!-- main photo with lower arc -->
    <path d="M470 421 A312 312 0 0 1 -5 243" fill="none" stroke="var(--teal)" stroke-width="10"/>
    <circle cx="296" cy="162" r="270" fill="url(#ceremonyTones)" role="img"
      aria-label="Photo: two women tying a ceremonial thread on the wrist of a young man in traditional dress"/>
    <!-- bottom wave -->
    <path d="M0 1096 C160 1155 360 1160 515 1116 C595 1066 655 1026 878 1016 V1200 H0 Z" fill="url(#waveGreen)"/>
    <path d="M0 1112 C160 1170 360 1175 520 1130 C600 1080 660 1040 878 1030 V1200 H0 Z" fill="var(--teal)"/>
  </svg>

  <div class="brand">TELVAMORE-QX</div>

  <h2 class="tab tab--platform">OUR PLATFORM</h2>
  <ul class="list platform">
    <li>A multi-vendor marketplace for the life science community to transact pre-market &amp; after-market materials &amp; equipment.</li>
    <li class="spaced">Researchers, manufactures, &amp; original suppliers can create an account to buy, sell, or donate materials.</li>
  </ul>

  <div class="step" style="left:11px;top:669px"><span class="step__num">1</span>Authentication<br>&amp; terms<br>of quality</div>
  <div class="step" style="left:121px;top:669px"><span class="step__num">2</span>Set up store</div>
  <div class="step" style="left:240px;top:663px"><span class="step__num">3</span>Seamlessly<br>trasnact &amp; request<br>for information</div>
  <div class="step" style="left:355px;top:663px"><span class="step__num">4</span>Check out<br>&amp; sign</div>

  <ul class="list features">
    <li>Part 11 compliant signature &amp; authentication.</li>
    <li>Leverages industry auditing skills to facilitate compliant and transparent transactions.</li>
    <li>Some of the best &amp; industry vendors &amp; software used.</li>
  </ul>

  <h2 class="tab tab--promise">OUR PROMISE</h2>
  <ul class="list promise">
    <li>A greener, more cost-efficient, &amp; quality driven supply chain through a collaborativelife sciences marketplace.</li>
  </ul>

  <h2 class="tab tab--benefits">BENEFITS</h2>
  <ul class="list benefits">
    <li>Reduce write-offs by selling excess &amp; obsolete materials, equipment, spare parts, etc.</li>
    <li>Buy quality materials at a reduced price.</li>
    <li>Market materials if an original supplier</li>
    <li>Donate material to researchers</li>
    <li>Acquire donated materials</li>
    <li>Collaborate &amp; consort to reduce supply chain risk such as mutual aid agreements, joint supplier audits, etc.</li>
  </ul>

  <p class="mission mission--aim"><strong>TELVAMORE-QX</strong> aspires to change the waste and risk paradigm in the life science industry.</p>
  <p class="mission mission--steward">We strive to make companies better stewards of their dollars &amp; our environment to transfer benefit to them...THE PATIENT</p>

  <section class="contact">
    <h2>CONTACT US</h2>
    <ul>
      <li><svg viewBox="0 0 12 12"><circle cx="6" cy="6" r="6" fill="#fff"/><rect x="3" y="4" width="6" height="4" fill="none" stroke="#147a68" stroke-width="1"/><path d="M3 4 L6 6.3 L9 4" fill="none" stroke="#147a68" stroke-width="1"/></svg>info@telvamoreqx.com</li>
      <li><svg viewBox="0 0 12 12"><circle cx="6" cy="6" r="6" fill="#fff"/><circle cx="6" cy="6" r="3.3" fill="none" stroke="#147a68" stroke-width="1"/><path d="M2.7 6 H9.3 M6 2.7 V9.3" stroke="#147a68" stroke-width=".8"/></svg>www.telvamoreqx.com</li>
      <li><svg viewBox="0 0 12 12"><circle cx="6" cy="6" r="6" fill="#fff"/><rect x="3.5" y="3" width="5" height="6" fill="#147a68"/></svg>Read our white paper</li>
    </ul>
  </section>
</main>
</body>
</html>
```